On-line Christmas Card design

We are a start-up management consulting business in New Zealand and are looking for a design for an on-line Christmas card.
We want to send the "card" out by embedded into an email. We need the whole design to be seen when the email is opened so landscape is probably better.

Target Market(s)

Our clients are senior executives in public and private sector organizations.

Industry/Entity Type

Management Consulting

Requirements
Must have
• Our logo somewhere in the design. Some source files are attached which show our stationery etc. Please don't change the colors of our logo in your design.
Use of our colors - green and gray.
A generic greeting - something referring to happy holidays, seasons greetings, etc rather than "Merry Christmas".

It's summer in NZ so no winter, snow scenes. If you are proposing a photo, then beach scenes are better. We would be interested in designs that are not photos.
Should not have
• Not religious.

```html
<!DOCTYPE html>
<html lang="en">
<head>
<meta charset="utf-8">
<title>Happy Holiday – Tidewell Consulting</title>
<link href="https://fonts.googleapis.com/css2?family=Lobster&family=Questrial&display=swap" rel="stylesheet">
<style>
  :root {
    --page: #ffffff;
    --brand-green: #7dc242;
    --text-green: #6aa834;
    --brand-grey: #939598;
    --text-grey: #8a8a8a;
    --band-grey: #939393;
    --ribbon-red: #d9201f;
    --ribbon-dark: #a8121a;
    --bow-light: #e8423a;
    --sand: #e2d4b8;
    --sea: #3fb5c6;
    --sky: #8fb6de;
    --palm: #6f7a3a;
  }
  html, body {
    margin: 0;
    width: 1200px;
    height: 925px;
    overflow: hidden;
    background: var(--page);
  }
  .canvas {
    position: relative;
    width: 1200px;
    height: 925px;
    font-family: "Questrial", "Century Gothic", sans-serif;
  }
  .card {
    position: absolute;
    left: 289px;
    top: 49px;
    width: 628px;
    height: 837px;
    background: var(--page);
  }
  .card-art {
    position: absolute;
    left: 0;
    top: 0;
  }
  .greeting {
    position: absolute;
    left: 0;
    width: 628px;
    text-align: center;
    margin: 0;
    line-height: 1;
  }
  .greeting-title {
    top: 440px;
    left: 8px;
    font-family: "Lobster", cursive;
    font-weight: 400;
    font-size: 50px;
    color: var(--ribbon-red);
    letter-spacing: 0.5px;
  }
  .greeting-from {
    top: 492px;
    left: -3px;
    font-size: 20px;
    color: var(--text-grey);
  }
  .brand {
    position: absolute;
    top: 518px;
    left: 0;
    width: 628px;
    display: flex;
    justify-content: center;
    align-items: center;
    gap: 8px;
    line-height: 1;
  }
  .brand-dot {
    width: 16px;
    height: 16px;
    border-radius: 50%;
    background: var(--brand-grey);
  }
  .brand-name {
    font-size: 40px;
    color: var(--brand-grey);
    letter-spacing: -0.8px;
  }
  .greeting-wish {
    top: 570px;
    font-size: 24px;
    color: var(--text-grey);
    letter-spacing: 1px;
  }
  .wishes {
    position: absolute;
    top: 610px;
    left: 0;
    width: 628px;
    margin: 0;
    padding: 0;
    list-style: none;
    text-align: center;
    font-size: 18.5px;
    line-height: 30.5px;
    color: var(--text-grey);
  }
  .wishes b { color: var(--text-green); font-weight: 400; }
  .wishes .closing { color: var(--text-green); }
  .contact {
    position: absolute;
    top: 786px;
    left: 226px;
    margin: 0;
    padding: 0;
    list-style: none;
    font-size: 13.5px;
    color: var(--text-grey);
    line-height: 15px;
  }
  .contact li { display: flex; align-items: center; gap: 6px; }
  .contact svg { flex: none; }
</style>
</head>
<body>
<main class="canvas">
  <section class="card">
    <svg class="card-art" width="628" height="837" viewBox="0 0 628 837">
      <defs>
        <linearGradient id="beachTones" x1="0" y1="0" x2="0" y2="1">
          <stop offset="0" stop-color="var(--sky)"/>
          <stop offset="0.42" stop-color="var(--sea)"/>
          <stop offset="0.58" stop-color="var(--sand)"/>
          <stop offset="1" stop-color="#d8c6a4"/>
        </linearGradient>
        <linearGradient id="palmShade" x1="0" y1="0" x2="1" y2="0">
          <stop offset="0" stop-color="var(--palm)" stop-opacity="0.55"/>
          <stop offset="0.6" stop-color="var(--palm)" stop-opacity="0"/>
        </linearGradient>
        <radialGradient id="bowTones" cx="0.5" cy="0.45" r="0.6">
          <stop offset="0" stop-color="var(--bow-light)"/>
          <stop offset="1" stop-color="var(--ribbon-dark)"/>
        </radialGradient>
      </defs>
      <rect class="top-band" x="0" y="0" width="628" height="16" fill="var(--brand-green)"/>
      <g role="img" aria-label="Photo of a tropical beach with palm trees, a hammock and a jetty over turquoise water">
        <polygon points="0,16 628,16 628,250 0,360" fill="url(#beachTones)"/>
        <polygon points="0,16 628,16 628,250 0,360" fill="url(#palmShade)"/>
      </g>
      <polygon class="ribbon" points="0,348 628,246 628,292 0,403" fill="var(--ribbon-red)"/>
      <polygon points="0,390 628,282 628,292 0,403" fill="var(--ribbon-dark)" opacity="0.45"/>
      <rect role="img" aria-label="Illustration of a red satin gift bow tied on the ribbon" x="201" y="234" width="228" height="204" rx="40" fill="url(#bowTones)"/>
      <rect x="0" y="16" width="2" height="811" fill="var(--band-grey)"/>
      <rect x="626" y="292" width="2" height="535" fill="var(--band-grey)"/>
      <rect class="bottom-band" x="0" y="827" width="628" height="10" fill="var(--band-grey)"/>
    </svg>

    <h1 class="greeting greeting-title">Happy Holiday!</h1>
    <p class="greeting greeting-from">from</p>
    <div class="brand">
      <span class="brand-dot"></span>
      <span class="brand-name">TidewellConsulting</span>
    </div>
    <p class="greeting greeting-wish">wishing you</p>

    <ul class="wishes">
      <li><b>peace</b> of mind, <b>prosperity</b> through the year</li>
      <li><b>happiness</b> that multiplies, <b>health</b> for you and yours</li>
      <li><b>fun</b> around every corner, <b>energy</b> to chase your dreams</li>
      <li class="closing">joy to fill your holidays!</li>
    </ul>

    <ul class="contact">
      <li>
        <svg width="12" height="9" viewBox="0 0 12 9"><rect x="0.5" y="0.5" width="11" height="8" fill="none" stroke="var(--brand-green)"/><path d="M0.5,0.5 L6,5 L11.5,0.5" fill="none" stroke="var(--brand-green)"/></svg>
        hello@tidewellconsulting.co.nz
      </li>
      <li>
        <svg width="12" height="12" viewBox="0 0 12 12"><circle cx="6" cy="6" r="5.5" fill="var(--brand-green)"/><path d="M1,6 H11 M6,1 V11" stroke="#fff" stroke-width="0.8"/></svg>
        www.tidewellconsulting.co.nz
      </li>
    </ul>
  </section>
</main>
</body>
</html>
```